New Flyer Design Project

I would like to purchase a customized version of a design you have previously submitted - https://www.plorvania.com/design/58204719

I want this to be something that looks really good.
We use this to explain our service agreements.
our website is www.bqumesh.net I want to stick with those colors.

```html
<!DOCTYPE html>
<html lang="en">
<head>
<meta charset="utf-8">
<title>BQM Support Plans – Flyers</title>
<link rel="stylesheet" href="https://fonts.googleapis.com/css2?family=Open+Sans:ital,wght@0,400;0,600;0,700;1,400&family=Oswald:wght@300;400&display=swap">
<style>
  :root {
    --backdrop: #d3cac5;
    --paper: #ffffff;
    --brand-red: #a3262a;
    --band-grey: #7a7a7a;
    --ink: #333333;
    --ink-soft: #555555;
    --row-tint: #f3e1dd;
    --rule: #c9c9c9;
    --photo-dark: #2d2d2f;
    --photo-mid: #6c6c70;
    --photo-light: #a9a9ad;
  }
  * { box-sizing: border-box; margin: 0; padding: 0; }
  html, body { width: 1200px; height: 418px; overflow: hidden; }
  body {
    background: var(--backdrop);
    font-family: "Open Sans", Arial, sans-serif;
    color: var(--ink);
    display: flex;
    justify-content: center;
    align-items: center;
    gap: 40px;
  }
  .flyer {
    position: relative;
    width: 284px;
    height: 404px;
    background: var(--paper);
    overflow: hidden;
  }
  .hero-photo {
    position: absolute; left: 0; top: 0; width: 100%; height: 114px;
    background: linear-gradient(90deg, var(--photo-dark) 0%, var(--photo-mid) 30%, var(--photo-light) 50%, var(--photo-mid) 70%, var(--photo-dark) 100%);
  }
  .brand {
    position: absolute; top: 26px; left: 0; width: 100%;
    text-align: center; color: #fff;
  }
  .brand-name {
    display: inline-flex; align-items: center; gap: 5px;
    font-weight: 700; font-size: 26px; letter-spacing: 2px; line-height: 1;
  }
  .brand-dot { width: 12px; height: 12px; border-radius: 50%; background: #fff; }
  .brand-tag { font-size: 5.6px; margin-top: 3px; }
  .title-band {
    position: absolute; top: 81px; left: 0; width: 100%; height: 27px;
    background: var(--brand-red); color: #fff;
    font-weight: 600; font-size: 14px; text-align: center; line-height: 27px;
  }
  .sub-band {
    position: absolute; top: 112px; left: 0; width: 100%; height: 19px;
    background: var(--band-grey); color: #fff;
    font-family: "Oswald", "Arial Narrow", sans-serif; font-weight: 300;
    font-size: 11px; text-align: center; line-height: 19px;
  }
  /* comparison table */
  .plan-table {
    position: absolute; top: 134px; left: 0; width: 100%;
    border-collapse: collapse; font-size: 4.8px; table-layout: fixed;
  }
  .plan-table th {
    background: var(--brand-red); color: #fff; height: 12px;
    font-weight: 700; font-size: 5px; text-align: center;
    border-right: 1px solid #fff;
  }
  .plan-table th:first-child { text-align: left; padding-left: 8px; font-size: 5.6px; }
  .plan-table td {
    height: 10.4px; padding: 0 4px 0 8px; line-height: 1.05;
    border-bottom: 0.5px solid var(--rule);
    border-right: 0.5px solid var(--rule);
  }
  .plan-table td.mark { text-align: center; padding: 0; font-size: 5.4px; }
  .plan-table tr:nth-child(even) td { background: var(--row-tint); }
  .plan-table tr.tall td { height: 14px; }
  .col-service { width: 62%; }
  .col-plus { width: 18%; }
  /* plan lists */
  .plan-heads {
    position: absolute; top: 111px; left: 0; width: 100%; height: 20px;
    display: grid; grid-template-columns: 1fr 1fr; gap: 2px;
  }
  .plan-head {
    background: var(--band-grey); color: #fff;
    font-family: "Oswald", "Arial Narrow", sans-serif; font-weight: 400;
    font-size: 11.5px; line-height: 20px; padding-left: 8px; white-space: nowrap;
  }
  .plan-lists {
    position: absolute; top: 135px; left: 0; width: 100%;
    display: grid; grid-template-columns: 1fr 1fr; gap: 6px; padding: 0 6px 0 8px;
  }
  .plan-list { list-style: none; font-size: 5.5px; color: var(--ink-soft); line-height: 1.35; }
  .plan-list.plus li { margin-bottom: 3.3px; }
  .plan-list.essentials li { margin-bottom: 5.2px; }
  .plan-list li.highlight { color: var(--brand-red); font-weight: 700; }
  /* footer */
  .contact {
    position: absolute; top: 351px; left: 0; width: 100%; text-align: center;
  }
  .call-label {
    color: var(--brand-red); font-size: 5.4px; font-weight: 600;
    text-align: left; padding-left: 58px; line-height: 1;
  }
  .contact-line { font-size: 10.5px; line-height: 1.15; font-weight: 600; color: #4a4a4a; }
  .contact-line .web { margin-left: 8px; color: #3a3a3a; }
  .address { font-size: 5.2px; font-weight: 700; color: #444; }
  .pricing-bar {
    position: absolute; left: 0; bottom: 0; width: 100%; height: 21px;
    background: linear-gradient(90deg, var(--brand-red) 0%, #b45a5b 45%, #f4e7e5 75%, #ffffff 100%);
    display: flex; align-items: center; justify-content: space-between; padding: 0 9px;
  }
  .pricing-note { color: #fff; font-style: italic; font-size: 5.4px; }
  .social { display: flex; gap: 6px; }
  .social span { width: 10px; height: 10px; border-radius: 50%; background: var(--brand-red); }
</style>
</head>
<body>

<!-- Comparison table flyer -->
<article class="flyer flyer-table">
  <div class="hero-photo" role="img" aria-label="Photo of a data center aisle lined with server racks"></div>
  <div class="brand">
    <div class="brand-name">BQM<span class="brand-dot"></span></div>
    <div class="brand-tag">bqumesh computing services</div>
  </div>
  <h1 class="title-band">BQM Support Plans</h1>
  <h2 class="sub-band">Serivice Plans Compairson Table</h2>
  <table class="plan-table">
    <colgroup><col class="col-service"><col class="col-plus"><col></colgroup>
    <thead>
      <tr><th>Services</th><th>Security Plus $75.00</th><th>IT Essentials $55.00 Per PC</th></tr>
    </thead>
    <tbody>
      <tr><td>Unlimited US bases Remote Help Desk Support</td><td class="mark">√</td><td class="mark">√</td></tr>
      <tr><td>Unlimited On-Site Support</td><td class="mark">√</td><td class="mark">Available</td></tr>
      <tr><td>Advanced Cybersecurity and Threat Hunting</td><td class="mark">√</td><td class="mark">Available</td></tr>
      <tr><td>Managed Antivirus Protection</td><td class="mark">√</td><td class="mark">√</td></tr>
      <tr><td>Multifactor Authentication Powered by Keyvora</td><td class="mark">√</td><td class="mark">Available</td></tr>
      <tr><td>Cyber Security Awareness Training</td><td class="mark">√</td><td class="mark">Available</td></tr>
      <tr><td>Enhanced Span Filtering</td><td class="mark">√</td><td class="mark">Available</td></tr>
      <tr><td>Internet Content Filtering</td><td class="mark">√</td><td class="mark">Available</td></tr>
      <tr><td>Proactive Security and System Monitoring</td><td class="mark">√</td><td class="mark">√</td></tr>
      <tr><td>Security and Vulnerability patching</td><td class="mark">√</td><td class="mark">√</td></tr>
      <tr><td>Backup and disaster recovery</td><td class="mark">√</td><td class="mark">√</td></tr>
      <tr><td>Network Management and Administration</td><td class="mark">√</td><td class="mark">√</td></tr>
      <tr class="tall"><td>Vantris Suite 365 Administration<br>and Configuration</td><td class="mark">√</td><td class="mark">√</td></tr>
      <tr><td>Vantris Nimbra Administration and Configuration</td><td class="mark">√</td><td class="mark">√</td></tr>
      <tr><td>Vantris Desko and Server Support</td><td class="mark">√</td><td class="mark">√</td></tr>
      <tr><td>Managed DNS</td><td class="mark">√</td><td class="mark">√</td></tr>
      <tr><td>Hardware and Software Procurement</td><td class="mark">√</td><td class="mark">√</td></tr>
      <tr><td>Assett Management</td><td class="mark">√</td><td class="mark">√</td></tr>
    </tbody>
  </table>
  <footer class="contact">
    <p class="call-label">Call us today</p>
    <p class="contact-line">(555) 014-2290<span class="web">www.bqumesh.net</span></p>
    <p class="address">48 Lanmere Court #210, Corvale, Texas 75990</p>
  </footer>
  <div class="pricing-bar">
    <span class="pricing-note">All Pricing is per month per PC</span>
    <div class="social"><span></span><span></span><span></span></div>
  </div>
</article>

<!-- Plan list flyer -->
<article class="flyer flyer-lists">
  <div class="hero-photo" role="img" aria-label="Photo of a data center aisle lined with server racks"></div>
  <div class="brand">
    <div class="brand-name">BQM<span class="brand-dot"></span></div>
    <div class="brand-tag">bqumesh computing services</div>
  </div>
  <h1 class="title-band">BQM Support Plans</h1>
  <div class="plan-heads">
    <h2 class="plan-head">Security Plus $75.00</h2>
    <h2 class="plan-head">IT Essentials $55.00 Per PC</h2>
  </div>
  <div class="plan-lists">
    <ul class="plan-list plus">
      <li>Unlimited US bases Remote Help Desk Support</li>
      <li class="highlight">On-Site Support</li>
      <li>Managed Endpoint Detection and Response (EDR) Network monitoring and management</li>
      <li>Managed Antivirus</li>
      <li class="highlight">MFA Multifactor Authentication</li>
      <li class="highlight">Security Awareness Training</li>
      <li class="highlight">Enhanced Spam Filtering</li>
      <li class="highlight">DNS filtering</li>
      <li>Proactive System Monitoring</li>
      <li>Security and Vulnerability patching</li>
      <li>Backup and disaster recovery</li>
      <li>Network Management</li>
      <li>Vantris 365 Administration</li>
      <li>Vantris Nimbra Administration</li>
      <li>Vantris Desko and Vantris Server support</li>
      <li>Managed DNS</li>
      <li>Hardware and Software Procurement</li>
      <li>Asset Management</li>
    </ul>
    <ul class="plan-list essentials">
      <li>Unlimited US bases Remote Help Desk Support "On-Site Support Available"</li>
      <li>Managed Endpoint Detection and Response (EDR) Network monitoring and management</li>
      <li>Managed Antivirus</li>
      <li>Security and Vulnerability patching</li>
      <li>Backup and disaster recovery</li>
      <li>Network Management</li>
      <li>Vantris 365 Administration</li>
      <li>Vantris 365 Backup</li>
      <li>Vantris Nimbra Administration</li>
      <li>Vantris Desko and Vantris Server support</li>
      <li>Managed DNS</li>
      <li>Hardware and Software Procurement</li>
      <li>Asset Management</li>
    </ul>
  </div>
  <footer class="contact">
    <p class="call-label">Call us today</p>
    <p class="contact-line">(555) 014-2290<span class="web">www.bqumesh.net</span></p>
    <p class="address">48 Lanmere Court #210, Corvale, Texas 75990</p>
  </footer>
  <div class="pricing-bar">
    <span class="pricing-note">All Pricing is per month per PC</span>
    <div class="social"><span></span><span></span><span></span></div>
  </div>
</article>

</body>
</html>
```